Marlow's Anvil BBQ Sauce Needs a Label

We are looking for a rustic label that would help our product stand out on a shelf. The company name is Marlow's Anvil. We are a new company looking to stand out on shelving with our amazing BBQ Sweet, Spicy and Rub. The label size needs to be 6.5" wide x 2.5" tall. I have taken a step in creating a label which is attached. This is just an idea for you to bring us an amazing retail ready look. On the left side of the label we need to have a 1 color flag with Made In USA. Also would need to have the address on the same side. Marlow's Anvil BBQ Sauce, Coconut Creek, FL 33073. The nutrition Facts are also needed. The information is correct but would need to be adjusted as to font and sizing. Image 7247 is what I have lightly put together and image 2495 is current logo on actual label. If you need any more guidance please let me know. Dobbs TangBlaze is an example of the pop we would like to see

Requirements
Must have
• Rustic Look
Nice to have
• Rustic look with a feeling similar to image 7247 that’s attached.
Should not have
• Same look as the original logo that’s on the actual label.

```html
<!DOCTYPE html>
<html lang="en">
<head>
<meta charset="utf-8">
<title>Marlow's Anvil BBQ Sauce – Label Set</title>
<link href="https://fonts.googleapis.com/css2?family=Roboto:wght@400;700;900&family=Roboto+Slab:wght@800&family=Dancing+Script:wght@700&display=swap" rel="stylesheet">
<style>
  :root{
    --ink:#1c1c1c;
    --brand-dark:#2e2e2e;
    --paper-light:#f3e6d2;
    --paper-mid:#ecd7b8;
    --paper-edge:#dfb98a;
    --sweet:#f2a03a;
    --spicy:#bd2030;
    --rub:#e6108a;
  }
  *{box-sizing:border-box;margin:0;padding:0}
  html,body{width:1119px;height:1200px;overflow:hidden;background:#fff}
  body{position:relative;font-family:"Roboto",Arial,sans-serif;color:var(--ink)}

  .label{
    position:absolute;left:131px;width:853px;height:328px;overflow:hidden;
    background:radial-gradient(ellipse at 45% 55%, var(--paper-light) 0%, var(--paper-mid) 55%, var(--paper-edge) 100%);
  }
  .label--sweet{top:87px;--flavor:var(--sweet)}
  .label--spicy{top:434px;--flavor:var(--spicy)}
  .label--rub{top:784px;--flavor:var(--rub)}

  /* left panel */
  .origin{position:absolute;left:15px;top:18px;width:110px}
  .origin svg{display:block;margin-left:25px}
  .origin__text{font-size:16px;margin-top:1px;letter-spacing:.1px;white-space:nowrap}
  .info{position:absolute;left:16px;top:142px;font-size:12.6px;line-height:15.4px;letter-spacing:.3px;white-space:nowrap}
  .info p{margin-bottom:3px}
  .info .address{margin-top:11px}

  /* brand block */
  .brand{position:absolute;left:238px;top:0;width:362px;height:328px;text-align:center}
  .brand__tag{font-family:"Dancing Script",cursive;font-size:19px;color:var(--brand-dark);position:absolute;top:24px;left:0;right:0}
  .brand__dot{position:absolute;left:166px;top:56px;width:30px;height:30px;border-radius:50%;background:var(--flavor)}
  .brand__name{font-family:"Roboto Slab",Georgia,serif;font-weight:800;color:var(--brand-dark);
    position:absolute;top:92px;left:0;right:0;font-size:40px;line-height:40px;text-transform:uppercase}
  .brand__product{position:absolute;top:182px;left:0;right:0;font-weight:900;font-size:22px;letter-spacing:1px}
  .brand__flavor{position:absolute;top:222px;left:0;right:0;font-family:"Dancing Script",cursive;font-size:40px;color:var(--flavor)}
  .net{position:absolute;left:514px;top:284px;font-size:20px;letter-spacing:.5px}

  /* nutrition facts */
  .facts{position:absolute;left:674px;top:11px;width:165px;height:307px;border:1px solid var(--ink);
    padding:2px 4px;font-size:9px;line-height:11px;overflow:hidden;white-space:nowrap}
  .facts__title{font-weight:900;font-size:21px;line-height:21px;letter-spacing:-.2px}
  .facts__line{display:flex;justify-content:space-between}
  .bar-thick{height:8px;background:var(--ink);margin-top:5px}
  .bar-mid{height:3px;background:var(--ink)}
  .small-bold{font-weight:900;font-size:7.6px;height:14px;line-height:13px;border-bottom:1px solid var(--ink)}
  .row{display:flex;justify-content:space-between;align-items:center;height:15px;border-bottom:1px solid var(--ink);font-size:9px}
  .row b{font-weight:900}
  .row--indent{padding-left:8px}
  .row--plain{border-bottom:none}
  .right{justify-content:flex-end}
  .vit{display:grid;grid-template-columns:44px 20px 1fr 20px;align-items:center;height:13px;font-size:8.6px;border-bottom:1px solid var(--ink)}
  .vit__val{text-align:right}
  .vit__dot{padding-left:13px}
  .vit__gap{padding-left:28px}
  .footnote{font-size:7.6px;line-height:10.4px;padding-top:1px;letter-spacing:-.2px;white-space:normal}
</style>
</head>
<body>

<!-- Sweet -->
<section class="label label--sweet">
  <div class="origin">
    <svg width="37" height="18" viewBox="0 0 37 18" aria-hidden="true">
      <g fill="var(--ink)">
        <circle cx="1" cy="1" r=".7"/><circle cx="4" cy="1" r=".7"/><circle cx="7" cy="1" r=".7"/><circle cx="10" cy="1" r=".7"/><circle cx="13" cy="1" r=".7"/>
        <circle cx="1" cy="4" r=".7"/><circle cx="4" cy="4" r=".7"/><circle cx="7" cy="4" r=".7"/><circle cx="10" cy="4" r=".7"/><circle cx="13" cy="4" r=".7"/>
        <circle cx="1" cy="7" r=".7"/><circle cx="4" cy="7" r=".7"/><circle cx="7" cy="7" r=".7"/><circle cx="10" cy="7" r=".7"/><circle cx="13" cy="7" r=".7"/>
        <rect x="16" y="0" width="21" height="2"/><rect x="16" y="4" width="21" height="2"/>
        <rect x="0" y="8" width="37" height="2"/><rect x="0" y="12" width="37" height="2"/><rect x="0" y="16" width="37" height="2"/>
      </g>
    </svg>
    <div class="origin__text">Made In USA</div>
  </div>
  <div class="info">
    <p>Refrigerate after<br>opening.</p>
    <p>Ingredients:<br>Tomato, Chili SAuce,<br>Vinegar, Worcester,<br>Sugar, Onion, Lemon,<br>Honet and Spices.</p>
    <p class="address">Marlow's Anvil<br>BBQ Sauce, Coconut<br>Creek, FL 33073.</p>
  </div>
  <div class="brand">
    <div class="brand__tag">Original Recipe</div>
    <div class="brand__dot"></div>
    <div class="brand__name">Marlow's<br>Anvil</div>
    <div class="brand__product">BBQ SAUCE</div>
    <div class="brand__flavor">Sweet</div>
  </div>
  <div class="net">16 oz</div>
  <div class="facts">
    <div class="facts__title">Nutrition Facts</div>
    <div>Serving Size 1 Tbsp. (18g)</div>
    <div class="facts__line"><span>Sering Per Container</span><span>25</span></div>
    <div class="bar-thick"></div>
    <div class="small-bold">Amount Per Serving</div>
    <div class="row"><span><b>Calories</b> 25</span><span>Calories from Fat 0</span></div>
    <div class="bar-mid"></div>
    <div class="row right"><b>% Daily Value*</b></div>
    <div class="row"><b>Total Fat</b><b>0%</b></div>
    <div class="row row--indent"><span>Saturated Fat 0g</span><b>0%</b></div>
    <div class="row row--indent"><span>Trans Fat 0g</span><span>0 g</span></div>
    <div class="row"><span><b>Cholesterol</b> 0mg</span><b>0%</b></div>
    <div class="row"><span><b>Sodium</b> 150mg</span><b>6%</b></div>
    <div class="row"><b>Total Carbohydrate</b><b>2%</b></div>
    <div class="row row--indent"><span>Dietary Fibre 0g</span><b>0%</b></div>
    <div class="row row--indent"><span>Sugar 6g</span><span></span></div>
    <div class="row row--plain"><span><b>Protein</b> 0.2g</span></div>
    <div class="bar-mid"></div>
    <div class="vit"><span>Vitamin A</span><span class="vit__val">1%</span><span class="vit__dot">•&nbsp;&nbsp;Vitamin C</span><span class="vit__val">6%</span></div>
    <div class="vit"><span>Calcium</span><span class="vit__val">1%</span><span class="vit__gap">Iron</span><span class="vit__val">1%</span></div>
    <div class="footnote">*Percent Daily Values are Based on 2.000 calorie diet. Your daily values may be higher or lower depending on your calorie needs.</div>
  </div>
</section>

<!-- Spicy -->
<section class="label label--spicy">
  <div class="origin">
    <svg width="37" height="18" viewBox="0 0 37 18" aria-hidden="true">
      <g fill="var(--ink)">
        <circle cx="1" cy="1" r=".7"/><circle cx="4" cy="1" r=".7"/><circle cx="7" cy="1" r=".7"/><circle cx="10" cy="1" r=".7"/><circle cx="13" cy="1" r=".7"/>
        <circle cx="1" cy="4" r=".7"/><circle cx="4" cy="4" r=".7"/><circle cx="7" cy="4" r=".7"/><circle cx="10" cy="4" r=".7"/><circle cx="13" cy="4" r=".7"/>
        <circle cx="1" cy="7" r=".7"/><circle cx="4" cy="7" r=".7"/><circle cx="7" cy="7" r=".7"/><circle cx="10" cy="7" r=".7"/><circle cx="13" cy="7" r=".7"/>
        <rect x="16" y="0" width="21" height="2"/><rect x="16" y="4" width="21" height="2"/>
        <rect x="0" y="8" width="37" height="2"/><rect x="0" y="12" width="37" height="2"/><rect x="0" y="16" width="37" height="2"/>
      </g>
    </svg>
    <div class="origin__text">Made In USA</div>
  </div>
  <div class="info">
    <p>Refrigerate after<br>opening.</p>
    <p>Ingredients:<br>Tomato, Chili SAuce,<br>Vinegar, Worcester,<br>Sugar, Onion, Lemon,<br>Honet and Spices.</p>
    <p class="address">Marlow's Anvil<br>BBQ Sauce, Coconut<br>Creek, FL 33073.</p>
  </div>
  <div class="brand">
    <div class="brand__tag">Original Recipe</div>
    <div class="brand__dot"></div>
    <div class="brand__name">Marlow's<br>Anvil</div>
    <div class="brand__product">BBQ SAUCE</div>
    <div class="brand__flavor">Spicy</div>
  </div>
  <div class="net">16 oz</div>
  <div class="facts">
    <div class="facts__title">Nutrition Facts</div>
    <div>Serving Size 1 Tbsp. (18g)</div>
    <div class="facts__line"><span>Sering Per Container</span><span>25</span></div>
    <div class="bar-thick"></div>
    <div class="small-bold">Amount Per Serving</div>
    <div class="row"><span><b>Calories</b> 25</span><span>Calories from Fat 0</span></div>
    <div class="bar-mid"></div>
    <div class="row right"><b>% Daily Value*</b></div>
    <div class="row"><b>Total Fat</b><b>0%</b></div>
    <div class="row row--indent"><span>Saturated Fat 0g</span><b>0%</b></div>
    <div class="row row--indent"><span>Trans Fat 0g</span><span>0 g</span></div>
    <div class="row"><span><b>Cholesterol</b> 0mg</span><b>0%</b></div>
    <div class="row"><span><b>Sodium</b> 150mg</span><b>6%</b></div>
    <div class="row"><b>Total Carbohydrate</b><b>2%</b></div>
    <div class="row row--indent"><span>Dietary Fibre 0g</span><b>0%</b></div>
    <div class="row row--indent"><span>Sugar 6g</span><span></span></div>
    <div class="row row--plain"><span><b>Protein</b> 0.2g</span></div>
    <div class="bar-mid"></div>
    <div class="vit"><span>Vitamin A</span><span class="vit__val">1%</span><span class="vit__dot">•&nbsp;&nbsp;Vitamin C</span><span class="vit__val">6%</span></div>
    <div class="vit"><span>Calcium</span><span class="vit__val">1%</span><span class="vit__gap">Iron</span><span class="vit__val">1%</span></div>
    <div class="footnote">*Percent Daily Values are Based on 2.000 calorie diet. Your daily values may be higher or lower depending on your calorie needs.</div>
  </div>
</section>

<!-- Rub -->
<section class="label label--rub">
  <div class="origin">
    <svg width="37" height="18" viewBox="0 0 37 18" aria-hidden="true">
      <g fill="var(--ink)">
        <circle cx="1" cy="1" r=".7"/><circle cx="4" cy="1" r=".7"/><circle cx="7" cy="1" r=".7"/><circle cx="10" cy="1" r=".7"/><circle cx="13" cy="1" r=".7"/>
        <circle cx="1" cy="4" r=".7"/><circle cx="4" cy="4" r=".7"/><circle cx="7" cy="4" r=".7"/><circle cx="10" cy="4" r=".7"/><circle cx="13" cy="4" r=".7"/>
        <circle cx="1" cy="7" r=".7"/><circle cx="4" cy="7" r=".7"/><circle cx="7" cy="7" r=".7"/><circle cx="10" cy="7" r=".7"/><circle cx="13" cy="7" r=".7"/>
        <rect x="16" y="0" width="21" height="2"/><rect x="16" y="4" width="21" height="2"/>
        <rect x="0" y="8" width="37" height="2"/><rect x="0" y="12" width="37" height="2"/><rect x="0" y="16" width="37" height="2"/>
      </g>
    </svg>
    <div class="origin__text">Made In USA</div>
  </div>
  <div class="info">
    <p>Refrigerate after<br>opening.</p>
    <p>Ingredients:<br>Tomato, Chili SAuce,<br>Vinegar, Worcester,<br>Sugar, Onion, Lemon,<br>Honet and Spices.</p>
    <p class="address">Marlow's Anvil<br>BBQ Sauce, Coconut<br>Creek, FL 33073.</p>
  </div>
  <div class="brand">
    <div class="brand__tag">Original Recipe</div>
    <div class="brand__dot"></div>
    <div class="brand__name">Marlow's<br>Anvil</div>
    <div class="brand__product">BBQ SAUCE</div>
    <div class="brand__flavor">Rub</div>
  </div>
  <div class="net">16 oz</div>
  <div class="facts">
    <div class="facts__title">Nutrition Facts</div>
    <div>Serving Size 1 Tbsp. (18g)</div>
    <div class="facts__line"><span>Sering Per Container</span><span>25</span></div>
    <div class="bar-thick"></div>
    <div class="small-bold">Amount Per Serving</div>
    <div class="row"><span><b>Calories</b> 25</span><span>Calories from Fat 0</span></div>
    <div class="bar-mid"></div>
    <div class="row right"><b>% Daily Value*</b></div>
    <div class="row"><b>Total Fat</b><b>0%</b></div>
    <div class="row row--indent"><span>Saturated Fat 0g</span><b>0%</b></div>
    <div class="row row--indent"><span>Trans Fat 0g</span><span>0 g</span></div>
    <div class="row"><span><b>Cholesterol</b> 0mg</span><b>0%</b></div>
    <div class="row"><span><b>Sodium</b> 150mg</span><b>6%</b></div>
    <div class="row"><b>Total Carbohydrate</b><b>2%</b></div>
    <div class="row row--indent"><span>Dietary Fibre 0g</span><b>0%</b></div>
    <div class="row row--indent"><span>Sugar 6g</span><span></span></div>
    <div class="row row--plain"><span><b>Protein</b> 0.2g</span></div>
    <div class="bar-mid"></div>
    <div class="vit"><span>Vitamin A</span><span class="vit__val">1%</span><span class="vit__dot">•&nbsp;&nbsp;Vitamin C</span><span class="vit__val">6%</span></div>
    <div class="vit"><span>Calcium</span><span class="vit__val">1%</span><span class="vit__gap">Iron</span><span class="vit__val">1%</span></div>
    <div class="footnote">*Percent Daily Values are Based on 2.000 calorie diet. Your daily values may be higher or lower depending on your calorie needs.</div>
  </div>
</section>

</body>
</html>
```